Onboarding project UI redesign

The web site is used to onboard clients via a video-identification process.
The end-user first tests his computer, then enters his order details and waits for an operator engagement.
When the operator engages the customer, they go through some identification steps together, ending on a contract signature page.

Target Market(s)

Finance B2C

Industry/Entity Type

Finance

Font styles to use
Sans Serif

Requirements
Must have
• Professional UI
• Design for mobile devices

```html
<!DOCTYPE html>
<html lang="en">
<head>
<meta charset="utf-8">
<title>Nordlane Bank – Confirm personal data</title>
<link rel="stylesheet" href="https://fonts.googleapis.com/css2?family=Roboto:wght@400;500;700&display=swap">
<style>
  :root{
    --brand:#0b4a8c;
    --brand-title:#0d4f94;
    --accent:#2f6ff3;
    --ink:#2b2b2b;
    --muted:#8a8a8a;
    --label:#6f6f6f;
    --field-border:#d6d6d6;
    --rail-line:#e6e6e6;
    --icon-bg:#efefef;
    --icon:#b9b9b9;
    --danger:#ec5a5a;
    --danger-bg:#fde9e9;
    --progress:#6cbf3a;
    --record:#e5322d;
    --chat:#5cb82f;
    --white:#ffffff;
  }
  *{box-sizing:border-box;margin:0;padding:0}
  html,body{width:1200px;height:746px;overflow:hidden;background:var(--white);font-family:"Roboto",sans-serif;color:var(--ink)}
  .screen{position:relative;width:1200px;height:746px}

  .topbar{position:absolute;left:0;top:0;width:1200px;height:44px;background:var(--brand);color:var(--white)}
  .brand{position:absolute;left:45px;top:12px;display:flex;align-items:center;gap:7px;font-size:15px;font-weight:500;letter-spacing:.5px}
  .brand-square{width:12px;height:12px;background:var(--white)}
  .clock{position:absolute;right:44px;top:15px;font-size:11px;display:flex;gap:14px}
  .clock strong{font-weight:700}

  .rail{position:absolute;left:0;top:44px;width:67px;height:702px;border-right:1px solid var(--rail-line)}
  .progress{position:absolute;left:7px;top:13px}
  .progress-label{position:absolute;left:7px;top:13px;width:54px;height:54px;display:flex;align-items:center;justify-content:center;font-size:14px;font-weight:700}
  .progress-label span{font-size:10px;font-weight:400;color:var(--muted)}
  .rail-btn{position:absolute;left:17px;width:34px;height:34px;border-radius:50%;background:var(--icon-bg);display:flex;align-items:center;justify-content:center}
  .rail-btn.hangup{background:var(--danger-bg)}

  .step{position:absolute;left:98px;top:62px}
  .step-num{font-size:10px;color:var(--ink)}
  .step-title{margin-top:6px;font-size:15px;font-weight:700;color:var(--brand-title)}

  .call-card{position:absolute;left:98px;top:136px;width:542px;height:570px;background:var(--white);box-shadow:0 4px 30px rgba(0,0,0,.08)}
  .client-video{position:absolute;left:0;top:0;width:542px;height:372px;background:linear-gradient(180deg,#f6ece2 0%,#d9cfc7 45%,#1f3553 100%)}
  .rec-timer{position:absolute;left:426px;top:13px;width:105px;height:31px;background:var(--brand);color:var(--white);font-size:12px;font-weight:700;display:flex;align-items:center;justify-content:center;gap:6px}
  .rec-dot{width:13px;height:13px;border-radius:50%;background:var(--record)}
  .operator-video{position:absolute;left:371px;top:313px;width:154px;height:97px;background:linear-gradient(135deg,#dfe6ee,#b8c4d2)}
  .dropzone{position:absolute;left:27px;top:410px;width:103px;height:130px;border:1px dashed #bdbdbd;border-radius:4px;text-align:center}
  .dropzone-hint{position:absolute;top:66px;width:100%;font-size:9px;color:#a9a9a9;line-height:11px}
  .browse{position:absolute;left:21px;top:93px;width:60px;height:20px;background:var(--accent);color:var(--white);font-size:8px;font-weight:500;display:flex;align-items:center;justify-content:center;border-radius:2px}
  .empty-title{position:absolute;left:152px;top:444px;font-size:18px;font-weight:700;color:#c4c4c4}
  .empty-note{position:absolute;left:152px;top:479px;font-size:10px}

  .intro{position:absolute;left:677px;top:63px;font-size:15px;line-height:22px;color:#3a3a3a}
  .field{position:absolute;height:44px;border:1px solid var(--field-border);border-radius:3px}
  .field-label{position:absolute;left:9px;top:-7px;padding:0 4px;background:var(--white);font-size:10px;font-weight:500;color:var(--label);letter-spacing:.2px}
  .field-value{position:absolute;left:17px;top:13px;font-size:15px;color:#8d8d8d}
  .field-icon{position:absolute;right:9px;top:9px}
  .confirm{position:absolute;left:677px;top:507px;width:119px;height:30px;background:var(--accent);color:var(--white);font-size:10px;font-weight:700;display:flex;align-items:center;justify-content:center;border-radius:2px}
  .chat{position:absolute;left:1130px;top:692px;width:30px;height:30px;border-radius:50%;background:var(--chat);display:flex;align-items:center;justify-content:center}
</style>
</head>
<body>
<div class="screen">
  <header class="topbar">
    <div class="brand"><span class="brand-square"></span>NORDLANE BANK</div>
    <div class="clock"><span>Friday, March 22, 2019</span><strong>11:12 AM</strong></div>
  </header>

  <nav class="rail">
    <svg class="progress" width="54" height="54" viewBox="0 0 54 54">
      <circle cx="27" cy="27" r="24" fill="none" stroke="#e3e3e3" stroke-width="4"/>
      <path d="M27 3 A24 24 0 0 1 50.5 22" fill="none" stroke="var(--progress)" stroke-width="4"/>
    </svg>
    <div class="progress-label">3<span>/11</span></div>

    <div class="rail-btn hangup" style="top:219px"><svg width="16" height="10" viewBox="0 0 16 10"><path d="M1 6c4-4 10-4 14 0l-2 2-2-1V5c-2-1-4-1-6 0v2l-2 1z" fill="var(--danger)"/></svg></div>
    <div class="rail-btn" style="top:278px"><svg width="14" height="14" viewBox="0 0 14 14" fill="none" stroke="var(--icon)" stroke-width="1.6"><path d="M8 6l5-5M9 1h4v4M6 8l-5 5M1 9v4h4"/></svg></div>
    <div class="rail-btn" style="top:323px"><svg width="14" height="14" viewBox="0 0 14 14" fill="none" stroke="var(--icon)" stroke-width="1.6"><rect x="5" y="1" width="4" height="7" rx="2"/><path d="M3 7a4 4 0 0 0 8 0M7 11v2M2 13L12 1"/></svg></div>
    <div class="rail-btn" style="top:368px"><svg width="16" height="12" viewBox="0 0 16 12" fill="none" stroke="var(--icon)" stroke-width="1.6"><rect x="1" y="3" width="10" height="7" rx="1"/><path d="M11 6l4-2v5l-4-2M2 11L14 1"/></svg></div>
    <div class="rail-btn" style="top:433px"><svg width="14" height="12" viewBox="0 0 14 12"><path d="M1 3h3l1-2h4l1 2h3v8H1z" fill="var(--icon)"/><circle cx="7" cy="7" r="2.2" fill="var(--icon-bg)"/></svg></div>
  </nav>

  <section class="step">
    <p class="step-num">Step 3.</p>
    <h1 class="step-title">CONFIRM PERSONAL DATA</h1>
  </section>

  <section class="call-card">
    <div class="client-video" role="img" aria-label="Live video of the client"></div>
    <div class="rec-timer"><span class="rec-dot"></span>00:03:17</div>
    <div class="operator-video" role="img" aria-label="Live video of the bank operator"></div>
    <div class="dropzone">
      <svg style="position:absolute;left:38px;top:22px" width="26" height="26" viewBox="0 0 26 26" stroke="#b5b5b5" stroke-width="1"><path d="M13 0v26M0 13h26"/></svg>
      <p class="dropzone-hint">Drag &amp; Drop<br>here or</p>
      <div class="browse">BROWSE</div>
    </div>
    <p class="empty-title">No documents uploaded yet.</p>
    <p class="empty-note">Upload your document here.</p>
  </section>

  <p class="intro">Now we will verify your data together.<br>If everything is correct, please press the CONFIRM button.</p>

  <form>
    <div class="field" style="left:677px;top:142px;width:483px"><span class="field-label">SIM CARD ID</span><span class="field-value">Enter</span></div>
    <div class="field" style="left:677px;top:200px;width:483px"><span class="field-label">NAME AND SURNAME</span><span class="field-value">Enter</span></div>
    <div class="field" style="left:677px;top:258px;width:237px"><span class="field-label">DATE OF BIRTH</span><span class="field-value">Select</span>
      <svg class="field-icon" width="30" height="28" viewBox="0 0 30 28" fill="none" stroke="#8a8a8a" stroke-width="1.6"><rect x="1" y="3" width="22" height="19" rx="2"/><path d="M1 8h22M6 1v4M18 1v4"/><path d="M5 12h2M10 12h2M15 12h2M5 16h2M10 16h2" stroke-width="2"/><circle cx="22" cy="20" r="6" fill="#fff"/><path d="M22 17v3h2"/></svg>
    </div>
    <div class="field" style="left:923px;top:258px;width:237px"><span class="field-label">PLACE OF BIRTH</span><span class="field-value">Enter</span></div>
    <div class="field" style="left:677px;top:316px;width:483px"><span class="field-label">NATIONAL INSURANCE NUMBER</span><span class="field-value">Enter</span></div>
    <div class="field" style="left:677px;top:374px;width:483px"><span class="field-label">ID DOCUMENT TYPE</span><span class="field-value">Choose</span>
      <svg class="field-icon" style="top:18px;right:14px" width="12" height="7" viewBox="0 0 12 7" fill="none" stroke="#8a8a8a" stroke-width="1.6"><path d="M1 1l5 5 5-5"/></svg>
    </div>
    <div class="field" style="left:677px;top:432px;width:283px"><span class="field-label">ID DOCUMENT NUMBER</span><span class="field-value">Enter</span></div>
    <div class="field" style="left:969px;top:432px;width:191px"><span class="field-label">VALID UNTIL</span><span class="field-value">Select</span>
      <svg class="field-icon" width="30" height="28" viewBox="0 0 30 28" fill="none" stroke="#8a8a8a" stroke-width="1.6"><rect x="1" y="3" width="22" height="19" rx="2"/><path d="M1 8h22M6 1v4M18 1v4"/><path d="M5 12h2M10 12h2M15 12h2M5 16h2M10 16h2" stroke-width="2"/><circle cx="22" cy="20" r="6" fill="#fff"/><path d="M22 17v3h2"/></svg>
    </div>
    <div class="confirm">CONFIRM</div>
  </form>

  <div class="chat"><svg width="18" height="14" viewBox="0 0 18 14"><ellipse cx="7" cy="6" rx="6.5" ry="5" fill="#fff"/><ellipse cx="11" cy="8" rx="6.5" ry="5" fill="none" stroke="#fff" stroke-width="1.4"/></svg></div>
</div>
</body>
</html>
```